Brochure Design Project

I would like for it took look a little different than my website, elegant, and classy. Our company wants to draw upper class customers to care for their home. We also focus private water taxi services for businesses to taxi their employees.

Target Market(s)

tourists, seasonal residents, property management.

Industry/Entity Type

Professional Service

Font styles to use
Serif

Requirements
Must have
• 2 sides

```html
<!DOCTYPE html>
<html lang="en">
<head>
<meta charset="utf-8">
<title>Pelican Cove Concierge Services – Trifold Brochure</title>
<link href="https://fonts.googleapis.com/css2?family=Lato:wght@300;400;700;900&display=swap" rel="stylesheet">
<style>
  :root{
    --red:#ef5a5c;
    --coral-top:#e9665f;
    --coral-bottom:#f28a7c;
    --ink:#2b2b2b;
    --grey:#5c5c5c;
    --paper:#ffffff;
    --stage:#ececec;
  }
  *{box-sizing:border-box;margin:0;padding:0}
  html,body{width:1200px;height:1200px;overflow:hidden;background:var(--stage)}
  body{font-family:'Lato',sans-serif;color:var(--ink)}
  .brochure{position:absolute;left:60px;top:175px;width:1080px;height:850px;display:flex;box-shadow:0 10px 30px rgba(0,0,0,.18)}
  .panel{position:relative;width:360px;height:100%;background:var(--paper);overflow:hidden}
  .panel + .panel{border-left:1px solid #e2e2e2}

  /* inside panel */
  .panel-about .photo-wood{height:125px;background:linear-gradient(135deg,#6b3f22,#9a5e35 45%,#5a3119)}
  .panel-about .rule{height:5px;background:var(--red)}
  .about-body{padding:16px 24px 0 24px;font-size:11px;line-height:1.36;color:var(--grey)}
  .about-body p{margin-bottom:8px}
  .about-body h3{color:var(--red);font-weight:400;font-size:14px;line-height:1.3;margin:2px 0 3px;border-bottom:1px solid var(--red);display:inline-block}

  /* middle panel */
  .panel-contact .request{padding:32px 28px 0;height:150px;font-size:13px;line-height:1.35}
  .request .accent{color:var(--red);font-weight:700;font-size:15px}
  .request .strong{font-weight:700}
  .photo-water{height:390px;background:linear-gradient(180deg,var(--coral-top),var(--coral-bottom));display:flex;flex-direction:column;align-items:center;justify-content:center;color:#fff}
  .brand-light{font-size:18px;letter-spacing:.28em;text-align:center;line-height:1.7;font-weight:400}
  .brand-mark{width:34px;height:34px;border:2px solid currentColor;border-radius:50%;margin-bottom:14px}
  .contact-list{list-style:none;margin:48px 0 0 34px;padding-left:22px;border-left:2px solid var(--red);font-size:15px;font-weight:700}
  .contact-list li{display:flex;align-items:flex-start;gap:12px;margin-bottom:16px}
  .contact-list svg{flex:none;margin-top:2px}

  /* cover panel */
  .cover-brand{height:150px;display:flex;flex-direction:column;align-items:center;justify-content:center;color:var(--ink)}
  .photo-wake{height:420px;background:linear-gradient(180deg,#f0a64b 0%,#c98a5a 18%,#8fa0ad 40%,#d8e1e6 62%,#2c3448 100%)}
  .headline{padding:26px 30px 0}
  .headline .line1{font-size:40px;font-weight:300;line-height:1}
  .headline .line2{font-size:44px;font-weight:900;color:var(--red);line-height:1.05}
  .headline .sub{font-size:19px;font-weight:300;color:var(--grey);margin-top:8px}
  .headline .sub2{font-size:21px;font-weight:900;margin-top:2px}
  .headline .sub2 em{font-style:normal;color:var(--red)}
  .url-pill{margin:18px 30px 0;padding:8px 16px;border-radius:20px;background:linear-gradient(180deg,#f6f6f6,#dcdcdc);font-size:14px;letter-spacing:.06em;color:var(--grey);text-align:center}
  .cover-strip{position:absolute;left:0;right:0;bottom:0;height:12px;background:var(--red)}
</style>
</head>
<body>
<main class="brochure">

  <section class="panel panel-about">
    <div class="photo-wood" role="img" aria-label="Close-up photo of a varnished wooden boat hull"></div>
    <div class="rule"></div>
    <div class="about-body">
      <p>Our concierge services are tailored to each request ensuring an exceptional client experience. We have the knowledge and resources through our trusted network of service providers to meet individual needs and preferences.</p>
      <p>Serving Pelican Cove and surrounding sister islands, Pelican Cove Concierge is the top innovator in the concierge service industry. Our company has the knowledge and resources through a trusted network of service providers to meet individual needs and preferences for our clients.</p>
      <h3>About Us</h3>
      <p>Founded in 2017 by Daniel and Claire Hollings, Pelican Cove Concierge provides the Palm Key area with an exclusive list of services for property management, including home services, rental guest liaison, and tailored concierge services. We are also offer private charters for water transportation to barrier islands, exclusive fishing adventures, and sightseeing tours.</p>
      <h3>Claire Hollings</h3>
      <p>As co-owner and operator of Pelican Cove Concierge, Claire combines her strong professional background in healthcare with a passion in caring for people in the community. Born and raised in Florida, Claire graduated from a local university with a Bachelor's Degree in Science Nursing. With years of business experience within the largest healthcare system in the state, she has held extraordinary positions that involve utilization management and centralized solutions. During her free time she enjoys fishing and boating with her family.</p>
      <h3>Daniel Hollings</h3>
      <p>With a strong corporate background and well-known experience working with one of the largest power and energy companies in the world, Daniel knows the importance of providing top level customer service. Also born and raised in Florida, Daniel completed an apprenticeship program in Miami where he earned his title as a Line Specialist. Now retired, throughout the years he continued to peruse his passion for competitive sports fishing where he developed long standing professional relationships within his community.</p>
    </div>
  </section>

  <section class="panel panel-contact">
    <div class="request">
      <p>Submit a request on our website</p>
      <p><span class="accent">PCSatYourRequest.com</span> or</p>
      <p>Call and speak with a concierge specialist</p>
      <p class="accent">(555) 014-2290</p>
      <p class="strong">Concierge services have grown far beyond that of a hotel lobby</p>
    </div>
    <div class="photo-water" role="img" aria-label="Photo of calm water glowing coral at sunset, with the company name">
      <div class="brand-mark"></div>
      <p class="brand-light">PELICAN COVE CONCIERGE<br>SERVICES L.L.C.</p>
    </div>
    <ul class="contact-list">
      <li><svg width="14" height="14" viewBox="0 0 24 24"><path fill="#ef5a5c" d="M6.6 10.8a15 15 0 0 0 6.6 6.6l2.2-2.2c.3-.3.7-.4 1-.2 1.1.4 2.3.6 3.6.6.6 0 1 .4 1 1V20c0 .6-.4 1-1 1A17 17 0 0 1 3 4c0-.6.4-1 1-1h3.5c.6 0 1 .4 1 1 0 1.3.2 2.5.6 3.6.1.3 0 .7-.2 1z"/></svg>(555) 014-2290</li>
      <li><svg width="14" height="14" viewBox="0 0 24 24"><circle cx="12" cy="12" r="9" fill="none" stroke="#ef5a5c" stroke-width="2.4"/><path d="M3 12h18M12 3c3 3 3 15 0 18M12 3c-3 3-3 15 0 18" fill="none" stroke="#ef5a5c" stroke-width="1.8"/></svg>www.pcsatyourrequest.com</li>
      <li><svg width="14" height="14" viewBox="0 0 24 24"><rect x="2" y="5" width="20" height="14" rx="2" fill="#ef5a5c"/><path d="M3 6l9 7 9-7" fill="none" stroke="#fff" stroke-width="1.8"/></svg>PCSatYourRequest@mailbox.com</li>
      <li><svg width="14" height="14" viewBox="0 0 24 24"><path fill="#ef5a5c" d="M12 2a7 7 0 0 0-7 7c0 5 7 13 7 13s7-8 7-13a7 7 0 0 0-7-7zm0 9.5A2.5 2.5 0 1 1 12 6.5a2.5 2.5 0 0 1 0 5z"/></svg>48 Harbor Palm Ln Seagrove<br>Fl 33900</li>
    </ul>
  </section>

  <section class="panel panel-cover">
    <div class="cover-brand">
      <div class="brand-mark"></div>
      <p class="brand-light">PELICAN COVE CONCIERGE<br>SERVICES L.L.C.</p>
    </div>
    <div class="photo-wake" role="img" aria-label="Photo of a boat wake behind twin outboard motors at sunset"></div>
    <div class="headline">
      <p class="line1">Your Request is</p>
      <p class="line2">Our Demand</p>
      <p class="sub">Call us with your request and</p>
      <p class="sub2">PCS will do the rest<em>!</em></p>
    </div>
    <p class="url-pill">www.pcsatyourrequest.com</p>
    <div class="cover-strip"></div>
  </section>

</main>
</body>
</html>
```